FRESH WEB DESIGN FOR A HEALTH - SOCIAL NETWORK

We are currently looking for a creative, fresh, vibrant, inspiring design for a new social network focused on health and nutrition for health professionals (namely nutritionists) and end-users.

Design requirements - IMPORTANT: please see attached file 'LumaCrest web site design scope' for the detailed brief.

The web site requires new design templates with inter-changeable banners and in some cases profile images. It's important for the website to communicate LumaCrest's core values and image which includes fun, vitality, freshness, life fulfillment, trust, integrity and loyalty to the two target groups. Imagery must have a consistent/inter-related theme across all communities, topics and resources, which need to be easily applied to the web site.To help engage our audience we are looking for something fresh and unique in the selected imagery/ theme/ design templates.

The chosen design will need to be applied to create a PDF, PowerPoint and business card template.

Please see attached file 'LumaCrest web site design scope' to view the LumaCrest web site, which is currently under development.

Nutrition

```html
<!DOCTYPE html>
<html lang="en">
<head>
<meta charset="utf-8">
<title>LumaCrest</title>
<link href="https://fonts.googleapis.com/css2?family=Exo+2:wght@600;700&family=Open+Sans:wght@400;600;700&display=swap" rel="stylesheet">
<style>
  :root {
    --purple: #6a2c8e;
    --lime: #b9d431;
    --lime-btn: #c0d72f;
    --blue: #0a8fd6;
    --orange: #f7a21b;
    --gray-head: #666666;
    --gray-text: #7a7a7a;
    --body-text: #444444;
    --band-gray: #ececec;
    --media-fill: #b7c9cf;
    --white: #ffffff;
  }
  * { margin: 0; padding: 0; box-sizing: border-box; }
  html, body { width: 886px; height: 1200px; overflow: hidden; background: var(--white); }
  body { position: relative; font-family: "Open Sans", Arial, sans-serif; color: var(--body-text); }

  .site-header { position: absolute; left: 0; top: 0; width: 886px; height: 58px; background: var(--purple); }
  .brand { position: absolute; left: 135px; top: 13px; display: flex; align-items: center; gap: 6px; }
  .brand-dot { width: 22px; height: 22px; border-radius: 50%; background: var(--lime); }
  .brand-name { font-family: "Exo 2", Arial, sans-serif; font-weight: 700; font-size: 22px; color: var(--lime); }
  .main-nav { position: absolute; top: 20px; left: 0; font-size: 10.5px; color: var(--white); }
  .main-nav span { position: absolute; white-space: nowrap; }
  .main-nav .active { color: var(--lime); font-weight: 700; }
  .search-icon { position: absolute; left: 741px; top: 22px; }

  .hero { position: absolute; left: 0; top: 58px; width: 886px; height: 228px;
    background: radial-gradient(ellipse at 55% 40%, #fdf3c4 0%, #f3df8e 45%, #c9d49a 75%, #9fc2bf 100%); }
  .hero-title { position: absolute; left: 232px; top: 64px; font-family: "Exo 2", Arial, sans-serif; font-weight: 700; font-size: 50px; line-height: 42px; letter-spacing: -1px; }
  .hero-title .l1 { display: block; color: #1594d8; }
  .hero-title .l2 { display: block; color: #f08a1c; padding-left: 42px; }
  .hero-arrow { position: absolute; top: 104px; width: 21px; height: 21px; background: var(--purple); }
  .hero-dots { position: absolute; left: 424px; top: 205px; display: flex; gap: 4px; }
  .hero-dots i { width: 7px; height: 7px; border-radius: 50%; background: #e0e0e0; display: block; }
  .hero-dots i.on { background: var(--blue); box-shadow: 0 0 0 1.5px #fff; }

  .welcome h1 { position: absolute; left: 135px; top: 305px; font-family: "Exo 2", Arial, sans-serif; font-weight: 700; font-size: 20px; color: var(--lime); }
  .welcome p { position: absolute; top: 346px; width: 300px; font-size: 7.3px; line-height: 12.3px; }
  .welcome b { color: #222; }

  .flower-band { position: absolute; left: 0; top: 475px; width: 886px; height: 228px;
    background: radial-gradient(ellipse at 50% 40%, #fcc35a 0%, #f7a62a 60%, #f29514 100%); }
  .flower-band h2 { position: absolute; top: 24px; width: 100%; text-align: center; font-family: "Exo 2", Arial, sans-serif; font-weight: 700; font-size: 18px; color: var(--white); }
  .flower-rule { position: absolute; left: 406px; top: 55px; width: 74px; height: 1px; background: rgba(255,255,255,.7); }
  .flower-band p { position: absolute; top: 68px; width: 100%; text-align: center; font-size: 13.5px; color: var(--white); }

  .video { position: absolute; left: 260px; top: 583px; width: 366px; height: 164px; border: 2px solid var(--white);
    background: var(--media-fill); box-shadow: 0 6px 8px -4px rgba(0,0,0,.45); }
  .play-btn { position: absolute; left: 165px; top: 70px; width: 34px; height: 21px; border-radius: 3px; background: rgba(40,40,40,.85); }

  .section-title { position: absolute; width: 100%; text-align: center; font-family: "Exo 2", Arial, sans-serif; font-weight: 700; font-size: 19px; color: var(--gray-head); }
  .new-users-lead { position: absolute; top: 821px; width: 100%; text-align: center; font-size: 15px; line-height: 19px; color: var(--gray-text); }
  .btn { position: absolute; height: 24px; border-radius: 5px; color: var(--white); font-size: 8.5px; font-weight: 700; text-align: center; line-height: 24px; }
  .btn-blue { left: 278px; width: 331px; background: var(--blue); }

  .existing-band { position: absolute; left: 0; top: 996px; width: 886px; height: 122px; background: var(--band-gray); }
  .btn-lime { left: 272px; top: 1061px; width: 342px; background: var(--lime-btn); }

  .footer-nav { position: absolute; top: 1140px; width: 100%; text-align: center; font-size: 9px; color: #222; }
  .footer-nav span.sep { margin: 0 6px; }
  .legal { position: absolute; top: 1163px; width: 100%; text-align: center; font-size: 6.5px; color: #333; }
  .legal span.sep { margin: 0 6px; }
</style>
</head>
<body>
  <header class="site-header">
    <div class="brand"><span class="brand-dot"></span><span class="brand-name">LumaCrest</span></div>
    <nav class="main-nav">
      <span class="active" style="left:466px">Home</span>
      <span style="left:515px">Topics</span>
      <span style="left:562px">Shop</span>
      <span style="left:604px">Sign Up</span>
      <span style="left:659px">FAQ</span>
      <span style="left:696px">Login</span>
    </nav>
    <svg class="search-icon" width="12" height="12" viewBox="0 0 12 12"><circle cx="5" cy="5" r="3.6" fill="none" stroke="#fff" stroke-width="1.7"/><line x1="7.6" y1="7.6" x2="11" y2="11" stroke="#fff" stroke-width="1.9" stroke-linecap="round"/></svg>
  </header>

  <section class="hero" role="img" aria-label="Banner photo: woman with outstretched arms under a sunny cloudy sky, colourful umbrella floating beside her">
    <div class="hero-title"><span class="l1">Enjoy</span><span class="l2">Life</span></div>
    <div class="hero-arrow" style="left:134px"><svg width="21" height="21" viewBox="0 0 21 21"><path d="M12 7 L8.5 10.5 L12 14" fill="none" stroke="#fff" stroke-width="1.6"/></svg></div>
    <div class="hero-arrow" style="left:732px"><svg width="21" height="21" viewBox="0 0 21 21"><path d="M9 7 L12.5 10.5 L9 14" fill="none" stroke="#fff" stroke-width="1.6"/></svg></div>
    <div class="hero-dots"><i class="on"></i><i></i><i></i><i></i></div>
  </section>

  <section class="welcome">
    <h1>Welcome to LumaCrest.</h1>
    <p style="left:135px">Lorem Ipsum has been the industry's standard dummy text ever since the 1500s, when an unknown printer took a galley of type and scrambled it to make a type specimen book. It has survived not only five centuries, but also the leap into electronic typesetting, remaining essentially unchanged. <b>It was popularised in the 1960s</b> with the release of Letterform sheets containing Lorem Ipsum passages, and more recently with desktop publishing software like Folio PageSmith including versions of Lorem Ipsum.</p>
    <p style="left:452px">Lorem Ipsum has been the industry's standard dummy text ever since the 1500s, when an unknown printer took a galley of type and scrambled it to make a type specimen book. <b>It has survived not only five centuries,</b> but also the leap into electronic typesetting, remaining essentially unchanged. It was popularised in the 1960s with the release of Letterform sheets containing Lorem Ipsum passages, and more recently with desktop publishing software like Folio PageSmith including versions of Lorem Ipsum.</p>
  </section>

  <section class="flower-band" role="img" aria-label="Warm orange sky backdrop with flying birds and a drifting feather">
    <h2>LUMACREST FLOWER</h2>
    <div class="flower-rule"></div>
    <p>Lorem Ipsum is simply dummy text of the printing and typesetting industry</p>
  </section>

  <div class="video" role="img" aria-label="Video still: two women in sun hats standing in a green field under a blue sky">
    <div class="play-btn"><svg width="34" height="21" viewBox="0 0 34 21"><path d="M14 6 L21 10.5 L14 15 Z" fill="#fff"/></svg></div>
  </div>

  <h2 class="section-title" style="top:784px">NEW USERS</h2>
  <p class="new-users-lead">Lorem Ipsum is simply dummy text of the<br>printing and typesetting industry</p>
  <div class="btn btn-blue" style="top:875px">Sign Up</div>
  <div class="btn btn-blue" style="top:908px">Ask a Question</div>
  <div class="btn btn-blue" style="top:941px">Explore</div>

  <section class="existing-band" role="img" aria-label="Light grey geometric chevron pattern background"></section>
  <h2 class="section-title" style="top:1017px">EXISTING USERS</h2>
  <div class="btn btn-lime">Login</div>

  <footer>
    <div class="footer-nav">HOME<span class="sep">•</span>TOPICS<span class="sep">•</span>SHOP<span class="sep">•</span>SIGN UP<span class="sep">•</span>FAQ<span class="sep">•</span>LOGIN</div>
    <div class="legal">© 2014 LumaCrest<span class="sep">I</span>Terms<span class="sep">I</span>Privacy</div>
  </footer>
</body>
</html>
```